Flyer für Immobilien (A4)
Zielgruppe
Es geht um den Verkauf von 2 Immobilien, welche auf diesem Flyer (DIN A4) mit Bildmateriel und kurzem Beschreib vorgestellt werden sollten.
Der Flyer ist für die Verteilung in Briefkästen von Privathaushältern gedacht.
Aufgabenstellung
Auf der Vorderseite sämtliche Texte, das Logo sowie die Aussenansicht der Liegenschaft (Bild 1) platzieren.
Auf der Rückseite können die restlichen Fotos in einer sinnvollen Aufteilung abgebildet werden.
Folgender Text sollte auf der Vorderseite gut aufgeteilt werden:
2x attraktive 4½-Zimmer-Wohnungen mit Balkon und schöner Aussicht ab Fr. 840‘000.—

```html
<!DOCTYPE html>
<html lang="de">
<head>
<meta charset="utf-8">
<title>Flyer Lindenweg 7</title>
<link rel="stylesheet" href="https://fonts.googleapis.com/css2?family=Kalam:wght@700&family=PT+Sans:wght@400;700&family=Arimo&display=swap">
<style>
  :root {
    --plum: #8d1a5b;
    --plum-deep: #7b144e;
    --white: #ffffff;
    --ink: #222222;
    --sky: #4d6fa3;
    --facade: #d9cfa6;
    --green: #a8f000;
    --room-light: #dcd7cf;
    --parquet: #b98a4e;
  }
  * { margin: 0; padding: 0; box-sizing: border-box; }
  html, body { width: 1200px; height: 830px; overflow: hidden; background: var(--white); }
  body { position: relative; font-family: "PT Sans", sans-serif; color: var(--ink); }

  .front { position: absolute; left: 0; top: 0; width: 587px; height: 830px; }
  .front-photo {
    position: absolute; left: 0; top: 0; width: 587px; height: 500px;
    background: linear-gradient(180deg, var(--sky) 0%, #8aa3c4 30%, var(--facade) 55%, #6f7a3c 85%, #4a5a2a 100%);
  }
  .front-band { position: absolute; left: 0; top: 0; width: 587px; height: 693px; }
  .tagline {
    position: absolute; left: 30px; top: 468px; width: 520px;
    font-family: "Kalam", cursive; font-weight: 700; font-size: 33px; color: var(--white);
    transform: rotate(-8deg); transform-origin: left bottom; white-space: nowrap; letter-spacing: 1px;
  }
  .front-address { position: absolute; left: 27px; top: 561px; font-size: 18.5px; font-weight: 700; color: var(--white); }
  .front-offer { position: absolute; left: 27px; top: 624px; font-size: 17.5px; line-height: 23px; color: var(--white); }
  .front-offer strong { font-weight: 700; }
  .contact { position: absolute; left: 27px; top: 725px; font-size: 13px; line-height: 16.6px; color: var(--ink); }
  .brand { position: absolute; left: 470px; top: 742px; display: flex; align-items: center; gap: 6px; color: var(--plum); font-size: 11px; font-weight: 700; }
  .brand-square { width: 12px; height: 12px; background: var(--plum); }

  .back { position: absolute; left: 613px; top: 0; width: 587px; height: 830px; }
  .back-header {
    position: absolute; left: 0; top: 0; width: 587px; height: 117px; background: var(--plum);
    color: var(--white); font-family: "Arimo", sans-serif; font-size: 18px; line-height: 22.5px; text-align: center; padding-top: 41px;
  }
  .photo { position: absolute; }
  .photo-bedroom { left: 0; top: 137px; width: 286px; height: 221px; background: linear-gradient(180deg, #e9e6e1 0%, #dedad4 55%, #7d7a78 80%, #9a9590 100%); }
  .photo-living { left: 301px; top: 137px; width: 286px; height: 221px; background: linear-gradient(180deg, #ecebe8 0%, #dcd9d2 55%, var(--parquet) 70%, #a87840 100%); }
  .photo-dining { left: 301px; top: 414px; width: 286px; height: 221px; background: linear-gradient(180deg, #efeeeb 0%, #e0ddd6 55%, var(--parquet) 72%, #a87840 100%); }
  .floorplan { left: 31px; top: 390px; width: 240px; height: 279px; background: linear-gradient(180deg, var(--green) 0%, var(--green) 78%, #f4f4f4 78%, #f4f4f4 100%); }
  .back-info {
    position: absolute; left: 0; top: 695px; width: 587px; height: 135px; background: var(--plum);
    color: var(--white); font-size: 11.2px; line-height: 14.3px;
  }
  .info-col { position: absolute; top: 18px; width: 245px; text-align: justify; }
  .info-col p + p { margin-top: 14px; }
  .info-left { left: 27px; }
  .info-right { left: 315px; text-align: left; }
</style>
</head>
<body>
  <section class="front">
    <div class="front-photo" role="img" aria-label="Aussenansicht des Mehrfamilienhauses mit Balkonen unter blauem Himmel"></div>
    <svg class="front-band" viewBox="0 0 587 693" aria-hidden="true">
      <path d="M0 452 C 180 500, 380 500, 587 445 L 587 693 L 0 693 Z" fill="var(--plum)"/>
    </svg>
    <div class="tagline">Immobilien mit mehr Sonnenseiten</div>
    <div class="front-address">Liegenschaft: Lindenweg 7, 6316 Talbach</div>
    <div class="front-offer">2 attraktive 4½-Zimmer-Wohnungen mit Balkon und<br>schöner Aussicht ab <strong>Fr. 840‘000.—</strong></div>
    <div class="contact">
      Für detaillierte Verkaufsunterlagen oder Besichtigungen:<br>
      Brunnmatt &amp; Partner AG<br>
      Tel.:&nbsp; 041 555 27 19<br>
      Mail: info@brunnmatt-partner.ch<br>
      Web: www.brunnmatt-partner.ch
    </div>
    <div class="brand"><span class="brand-square"></span>Brunnmatt &amp; Partner AG</div>
  </section>

  <section class="back">
    <header class="back-header">Zentrale und ruhige 4½-Zimmer-Wohnungen mit Balkon<br>Liegenschaft: Lindenweg 7, 6316 Talbach</header>
    <div class="photo photo-bedroom" role="img" aria-label="Schlafzimmer mit Doppelbett und Bild an der Wand"></div>
    <div class="photo photo-living" role="img" aria-label="Wohnzimmer mit Parkettboden und Sofa"></div>
    <div class="photo floorplan" role="img" aria-label="Grundriss der 4½-Zimmer-Wohnung mit Schlafzimmern, Bad, Küche, Wohnen, Essen und Balkon"></div>
    <div class="photo photo-dining" role="img" aria-label="Offener Essbereich mit Tisch und Parkettboden"></div>
    <div class="back-info">
      <div class="info-col info-left">
        Die ruhige und doch zentral gelegene Liegenschaft befindet sich nur wenige Gehminuten vom Dorfzentrum. Optimale Ausrichtung, öffentliche Verkehrsmittel, Post, Banken, diverse Einkaufsmöglichkeiten, Restaurants, Freizeit- und Erholungsmöglichkeiten sind ebenfalls zu Fuss erreichbar und bieten die ideale Wohnlage.
      </div>
      <div class="info-col info-right">
        <p>Fordern Sie unverbindlich unsere Verkaufsunterlagen an.&nbsp; Tel.: +41 41 555 27 19</p>
        <p>Gerne stehen wir Ihnen für ein persönliches Beratungsgespräch und weitere Informationen zur Verfügung.<br>Brunnmatt &amp; Partner AG - Seeberg</p>
      </div>
    </div>
  </section>
</body>
</html>
```